Vantrel LLC banner ad design project

I want banner advertisements designed in various ad formats-the most popular sizes according to Brindle Adspace (600x450, 300x250, 250x250, 120x600).
Please put in the ads a picture of the bottle (attached) and a picture of a slim woman/man (preferably woman, as I am targetting a largely female audience) in the advertisement.
As for the text of the ads, I'd like for there to be something like the following:
"Lose 15 lbs in 3 months"
"Lose weight with traditional Chinese medicine"
"Lose weight using ancient Chinese herbs"
Also please feel free to use other text using some of the articles on my site, which can be found at the following link:
http://www.vantrel-shop.com/
Thanks, and if you have any additional questions, please don't hesitate to ask.
Additional notes: would also like for you to follow the color scheme on my website (orange, green) for the most part, although please when submitting different ads make sure to include other color schemes, as some of those color schemes may work better for the ads than the green/orange color scheme.
I've also attached an ad from Plenafirm that should give you an idea of something similar I'm looking for (though please submit multiple ideas)!

```html
<!DOCTYPE html>
<html lang="en">
<head>
<meta charset="utf-8">
<title>Vantrel Web Banner Ad Design</title>
<link rel="stylesheet" href="https://fonts.googleapis.com/css2?family=Open+Sans:ital,wght@0,400;0,600;0,700;0,800;1,600&display=swap">
<style>
  :root {
    --page: #ffffff;
    --page-edge: #cfcfcf;
    --caption: #8c8c8c;
    --peach: #fde6d4;
    --orange: #f2853a;
    --orange-deep: #e9661f;
    --green: #2f7f2c;
    --green-dark: #245f1f;
    --band: #2d6a22;
    --band-light: #3f8a2c;
    --natural-text: #f3e46a;
    --url: #f4c430;
    --brand: #ea6a22;
    --copy: #7b3612;
    --skin: #e7c2a8;
    --skin-light: #f6e2d4;
  }
  * { margin: 0; padding: 0; box-sizing: border-box; }
  html, body { width: 848px; height: 1200px; overflow: hidden; background: var(--page); }
  body { position: relative; font-family: "Open Sans", Arial, sans-serif; }

  .sheet {
    position: absolute; inset: 0;
    border: 1px solid var(--page-edge);
  }

  .caption {
    position: absolute;
    font-size: 10px; font-style: italic; font-weight: 600;
    color: var(--caption); letter-spacing: 0.3px;
  }
  .sheet-title {
    position: absolute; left: 37px; top: 1138px;
    font-size: 11px; font-style: italic; font-weight: 600;
    color: var(--caption); letter-spacing: 0.4px;
  }

  .banner {
    position: absolute; overflow: hidden;
    background: radial-gradient(ellipse at 30% 10%, var(--peach) 0%, #f9c7a3 35%, var(--orange) 75%, var(--orange-deep) 100%);
  }
  .banner > * { position: absolute; }
  .band { left: 0; top: 0; width: 100%; height: 100%; }

  .model-photo {
    left: 0; top: 0; height: 100%;
    background: linear-gradient(90deg, var(--skin-light) 0%, var(--skin) 55%, #f3ddd0 85%, rgba(246,226,212,0) 100%);
  }
  .bottle-photo {
    border-radius: 14% 14% 10% 10% / 8% 8% 6% 6%;
    background: linear-gradient(90deg, #d9d9d6 0%, #ffffff 35%, #f4f4f1 70%, #c9c9c4 100%);
    box-shadow: 0 4px 10px rgba(90,40,10,0.25);
  }

  .headline {
    font-weight: 800; color: var(--green); text-align: center;
    line-height: 1; letter-spacing: -0.5px; white-space: nowrap;
  }
  .subhead {
    font-weight: 600; color: var(--green); text-align: center;
    line-height: 1; white-space: nowrap;
  }
  .brand-name {
    font-weight: 600; color: var(--brand); text-align: center;
    line-height: 1; white-space: nowrap;
  }
  .offer {
    font-weight: 800; color: var(--green); text-align: center;
    line-height: 1.02; white-space: nowrap;
  }
  .natural-tag {
    background: var(--green-dark); color: var(--natural-text);
    font-weight: 700; text-align: center; letter-spacing: 0.5px;
    white-space: nowrap;
  }
  .benefits { list-style: none; }
  .benefits li { position: relative; color: var(--copy); font-weight: 600; }
  .benefits svg { position: absolute; }
  .site-url {
    color: var(--url); font-weight: 700; white-space: nowrap; letter-spacing: 0.3px;
  }
</style>
</head>
<body>
<div class="sheet">

  <!-- 600 x 450 -->
  <section class="banner banner-large" style="left:121px; top:73px; width:614px; height:460px;">
    <svg class="band" viewBox="0 0 614 460" preserveAspectRatio="none">
      <path d="M0 412 C180 420 380 408 614 388 L614 460 L0 460 Z" fill="var(--band)"/>
      <path d="M0 412 C180 420 380 408 614 388 L614 394 C380 414 180 426 0 418 Z" fill="var(--band-light)"/>
    </svg>
    <div class="model-photo" role="img" aria-label="Slim woman in white top and shorts measuring her waist with a yellow tape measure" style="width:190px;"></div>
    <div class="headline" style="left:190px; top:14px; width:410px; font-size:57px;">LOSE WEIGHT</div>
    <div class="subhead" style="left:190px; top:70px; width:410px; font-size:21px;">USING ANCIENT CHINESE HERBS</div>
    <div class="bottle-photo" role="img" aria-label="White supplement bottle with herbal label" style="left:206px; top:126px; width:158px; height:264px;"></div>
    <div class="brand-name" style="left:415px; top:158px; width:180px; font-size:33px;">VANTREL</div>
    <div class="offer" style="left:415px; top:204px; width:180px; font-size:29px;">TRY NOW<br>RISK FREE</div>
    <div class="natural-tag" style="left:433px; top:268px; width:143px; height:20px; font-size:14px; line-height:20px;">100% NATURAL</div>
    <ul class="benefits" style="left:430px; top:298px; width:180px; font-size:15px; line-height:19px;">
      <li>Clinically proven weight loss tool
        <svg viewBox="0 0 24 20" style="left:-40px; top:6px; width:28px; height:22px;"><path d="M2 11 L9 18 L22 2" fill="none" stroke="var(--green-dark)" stroke-width="3.5" stroke-linecap="round" stroke-linejoin="round"/></svg></li>
      <li style="margin-top:6px;">Targets excess belly fat and increases metabolism
        <svg viewBox="0 0 24 20" style="left:-40px; top:2px; width:28px; height:22px;"><path d="M2 11 L9 18 L22 2" fill="none" stroke="var(--green-dark)" stroke-width="3.5" stroke-linecap="round" stroke-linejoin="round"/></svg></li>
    </ul>
    <div class="site-url" style="left:388px; top:432px; width:214px; font-size:14.5px; text-align:right;">WWW.VANTREL-SHOP.COM</div>
  </section>
  <div class="caption" style="left:121px; top:544px;">(600PX X 450PX)</div>

  <!-- 300 x 250 -->
  <section class="banner banner-medium" style="left:121px; top:600px; width:307px; height:255px;">
    <svg class="band" viewBox="0 0 307 255" preserveAspectRatio="none">
      <path d="M0 226 C100 232 200 224 307 212 L307 255 L0 255 Z" fill="var(--band)"/>
    </svg>
    <div class="model-photo" role="img" aria-label="Slim woman measuring her waist with a yellow tape measure" style="width:88px;"></div>
    <div class="headline" style="left:72px; top:8px; width:226px; font-size:30px;">LOSE WEIGHT</div>
    <div class="subhead" style="left:72px; top:39px; width:226px; font-size:11.5px;">USING ANCIENT CHINESE HERBS</div>
    <div class="bottle-photo" role="img" aria-label="White supplement bottle with herbal label" style="left:82px; top:68px; width:84px; height:166px;"></div>
    <div class="brand-name" style="left:195px; top:84px; width:105px; font-size:18px;">VANTREL</div>
    <div class="offer" style="left:195px; top:109px; width:105px; font-size:16.5px;">TRY NOW<br>RISK FREE</div>
    <div class="natural-tag" style="left:203px; top:145px; width:86px; height:12px; font-size:8.5px; line-height:12px;">100% NATURAL</div>
    <ul class="benefits" style="left:206px; top:160px; width:96px; font-size:8.5px; line-height:10.5px;">
      <li>Clinically proven weight loss tool
        <svg viewBox="0 0 24 20" style="left:-18px; top:2px; width:14px; height:12px;"><path d="M2 11 L9 18 L22 2" fill="none" stroke="var(--green-dark)" stroke-width="3.5" stroke-linecap="round" stroke-linejoin="round"/></svg></li>
      <li style="margin-top:3px;">Targets excess belly fat and increases metabolism
        <svg viewBox="0 0 24 20" style="left:-18px; top:1px; width:14px; height:12px;"><path d="M2 11 L9 18 L22 2" fill="none" stroke="var(--green-dark)" stroke-width="3.5" stroke-linecap="round" stroke-linejoin="round"/></svg></li>
    </ul>
    <div class="site-url" style="left:170px; top:237px; width:130px; font-size:8.5px; text-align:right;">WWW.VANTREL-SHOP.COM</div>
  </section>
  <div class="caption" style="left:121px; top:866px;">(300PX X 250PX)</div>

  <!-- 250 x 250 -->
  <section class="banner banner-square" style="left:479px; top:600px; width:256px; height:255px;">
    <svg class="band" viewBox="0 0 256 255" preserveAspectRatio="none">
      <path d="M0 226 C90 232 170 224 256 212 L256 255 L0 255 Z" fill="var(--band)"/>
    </svg>
    <div class="model-photo" role="img" aria-label="Slim woman measuring her waist with a yellow tape measure" style="width:74px;"></div>
    <div class="headline" style="left:72px; top:8px; width:178px; font-size:24px;">LOSE WEIGHT</div>
    <div class="subhead" style="left:72px; top:34px; width:178px; font-size:10px;">USING ANCIENT CHINESE HERBS</div>
    <div class="bottle-photo" role="img" aria-label="White supplement bottle with herbal label" style="left:80px; top:86px; width:72px; height:134px;"></div>
    <div class="brand-name" style="left:152px; top:84px; width:98px; font-size:17px;">VANTREL</div>
    <div class="offer" style="left:152px; top:109px; width:98px; font-size:15.5px;">TRY NOW<br>RISK FREE</div>
    <div class="natural-tag" style="left:158px; top:144px; width:80px; height:12px; font-size:8px; line-height:12px;">100% NATURAL</div>
    <ul class="benefits" style="left:157px; top:160px; width:94px; font-size:8px; line-height:10px;">
      <li>Clinically proven weight loss tool</li>
      <li style="margin-top:3px;">Targets excess belly fat and increases metabolism</li>
    </ul>
    <div class="site-url" style="left:120px; top:237px; width:130px; font-size:8.5px; text-align:right;">WWW.VANTREL-SHOP.COM</div>
  </section>
  <div class="caption" style="left:479px; top:866px;">(250PX X 250PX)</div>

  <!-- 600 x 120 -->
  <section class="banner banner-wide" style="left:118px; top:920px; width:613px; height:122px;">
    <svg class="band" viewBox="0 0 613 122" preserveAspectRatio="none">
      <path d="M0 104 C200 108 400 98 613 84 L613 122 L0 122 Z" fill="var(--band)"/>
    </svg>
    <div class="model-photo" role="img" aria-label="Slim woman measuring her waist with a yellow tape measure" style="width:96px;"></div>
    <div class="headline" style="left:88px; top:12px; width:320px; font-size:46px;">LOSE WEIGHT</div>
    <div class="subhead" style="left:88px; top:58px; width:320px; font-size:15.5px;">USING ANCIENT CHINESE HERBS</div>
    <div class="natural-tag" style="left:172px; top:83px; width:150px; height:20px; font-size:15px; line-height:20px;">100% NATURAL</div>
    <div class="bottle-photo" role="img" aria-label="White supplement bottle with herbal label" style="left:414px; top:2px; width:66px; height:118px;"></div>
    <div class="brand-name" style="left:488px; top:44px; width:118px; font-size:22px;">VANTREL</div>
    <div class="site-url" style="left:470px; top:104px; width:136px; font-size:9px; text-align:right;">WWW.VANTREL-SHOP.COM</div>
  </section>
  <div class="caption" style="left:118px; top:1057px;">(600PX X 120PX)</div>

  <div class="sheet-title">VANTREL WEB BANNER AD DESIGN</div>
</div>
</body>
</html>
```